Is your Will up to date?

We need a flyer that invites people to ask themselves if their Will is up to date.
In addition it is a known fact that people do not adjust their Will as often as they should to reflect their current wishes and circumstances.
Also, a large number of people end up having their estate pay taxes
that could be avoided if correct planning is in place.
We are offering a free of charge service the carry out a check to make sure families have in place a Will that suits their needs and circumstances and that has taken into account the tax positions and impact fully with a view to having the estate as tax efficient as possible.
A Will service is also part of the family check up.

Below is the suggested text for the flyer

A Will is one of the most important documents that we should all have. Many people are aware that if they die without having made a Will, then intestate rules apply which means in simple terms, that family assets and cash could end up in the hands of the Treasury.

While many people have looked at and acted upon creating a Will, it is fair to say that for many, the terms and wishes of the Will are often outdated. It is easy to assume that amending a Will frequently is a complicated process which it need not be.

An individual or a family Will is most important in order to ensure that upon death, your estate is dealt with and distributed in accordance with your wishes. This is also to ensure that any family are looked after by those provisions. Not only may family changes and additions affect a family Will, but there are also life changing situations that can have an effect.

Additionally, consideration needs to be given regularly to the current tax position, with specific regard to Inheritance Tax and how estate values can be legitimately reduced resulting in less tax to pay.

At Hartwell & Company we have the advantage of our Chartered Accountancy practice background, as well as also being Independent Financial Advisers. We are therefore well placed to advise families on the creation or updating of their Will, and to give advice on how to minimise tax payments.

Even for individuals and families that have had no significant changes in circumstances for many years, very often the beneficiaries may need to be updated, and even the appointment of Executors and Trustees needs to be addressed because very often, these instructions are considerably out of date.

A Will and all of its complex implications should be reviewed every one or two years and it is an extremely simple process to do this with our assistance.

So far as minimising payments for tax there are a wide range of effective methods that help do this. As general examples, there can be gifts made to family or a partner, gifts to friends, charitable donations, the use of insurance products to help settle tax liability as well as looking at placing assets into Trust. We have a wealth of experience in setting up the different types of Trust that exist and can help you easily understand how they would work for you.

When looking at the preparation of a Will, there are hundreds of questions that could be considered appropriate. However, with our experience and knowledge, and bespoke software this process can be covered within an initial meeting of less than one hour. You will have the re-assurance of knowing that every aspect has been carefully considered in preparing a Will to your circumstances and wishes.

The initial meeting and any follow up meetings are completely free of all cost and charges, and can be held at either our offices, or at your home if preferred.

We can just as easily deal with the process over the telephone if more convenient. Thereafter, we will prepare a draft Will for you, and give you confirmation as to the charges. In most cases, an individual or family Will would not normally involve charges in excess of £100.

So far as mitigating possible Inheritance Tax liabilities on the estate, we also offer the benefit of an asset and investment review at no cost. The individual or family assets are carefully considered, along with your requirements of income and growth and any specific requests or wishes that you wish to build into any trust or other methods of your choosing.

At the initial meeting or conference call we discuss all of these implications and will prepare a report and recommendations for your consideration, again free of charge. If you decide to act upon any of the recommendations, then any fees can be discussed and agreed at that stage.

All in all, whether you require assistance in preparing or updating a Will, or receiving independent advice regarding your estate assets or investments, these functions are carried out by us at no initial costs or charges.

At every step of the way there are never hidden charges or fees that you will be asked to be paid. We have over 30 years of experience in these market places, and value the service we give our clients and the reputation we gain from it.

We consider the review of a Will should be carried out at a minimum of every two years and it is a very small financial budget to allow for, against having the satisfaction of knowing these important matters are reflecting your current views, circumstances and wishes.

The same can be said for any trust and investment matters and any estate advice given. We are extremely proud and confident of the service we provide, and if any of our clients decide they do not wish to act upon the advice given, then they at least have had the benefit of a thorough review together with a recommendation without obligations of any sort.

To discuss these matters further or to make arrangements for a meeting please call our offices or email to derek@hartwellco-mail.co.uk

Content will be uploaded with next 24 hours

I am updating the brief with the wording.
It needs to be spread over the front and back of the flyer in an easy to read non boring design

Our firm logo will be updated shorty plus our Institute logo
Please make the flyer as catchy and interesting as possible.
Its a relatively boring topic for most people so it has to be eye catching rather than reading a page in a book

We will increase the budget if we are presented with a design we really like

Please note slightly amended text uploaded today

Target Market(s)

middle to upper class residents

Industry/Entity Type

Investment

Requirements
Must have
• Web address
Easy to read and understand
To look and feel catchy and not like reading a book
Some catchy graphics about tax, money, families etc

Fields where I can easily insert text and other details

```html
<!DOCTYPE html>
<html lang="en">
<head>
<meta charset="utf-8">
<title>Is Your Will Up To Date? – Hartwell &amp; Company flyer</title>
<link rel="stylesheet" href="https://fonts.googleapis.com/css2?family=Arimo:ital,wght@0,400;0,700;1,400&family=Open+Sans:wght@400;600&family=Roboto+Condensed:wght@700&display=swap">
<style>
  :root{
    --paper:#ffffff;
    --ink-light:#ffffff;
    --photo-dark:#2c2c2c;
    --photo-mid:#6b6b6b;
    --photo-light:#c9c9c9;
    --logo-box:#3a2623;
    --title-red:#dc4a2e;
    --top-strip:#3b2a28;
    --will-yellow:#e9e08e;
    --will-yellow-dark:#7d7a47;
    --tax-coral:#e2826b;
    --tax-coral-dark:#8a4236;
    --help-blue:#4fb4da;
    --help-blue-dark:#2e6f86;
    --offer-green:#c7d790;
    --offer-green-dark:#6f7c4a;
    --panel-grey:#6e6f71;
  }
  *{box-sizing:border-box;margin:0;padding:0}
  html,body{width:1200px;height:752px;overflow:hidden;background:var(--paper)}
  body{position:relative;font-family:"Open Sans",Arial,sans-serif;color:var(--ink-light)}

  /* Front page */
  .front{position:absolute;left:11px;top:11px;width:562px;height:732px;overflow:hidden}
  .front-strip{position:absolute;left:0;top:0;width:100%;height:13px;background:var(--top-strip)}
  .front-photo{position:absolute;left:0;top:13px;width:100%;height:719px;
    background:linear-gradient(180deg,#1f1f1f 0%,#4a4a4a 18%,#8a8a8a 42%,#5b5b5b 58%,#9d9d9d 72%,#cfcfcf 86%,#7a7a7a 100%)}
  .logo-box{position:absolute;left:325px;top:76px;width:237px;height:77px;background:var(--logo-box);
    display:flex;align-items:center;padding-left:22px;
    font-family:"Roboto Condensed",Arial,sans-serif;font-weight:700;font-size:24px}
  .title-band{position:absolute;left:0;top:432px;width:326px;height:133px;background:var(--title-red);opacity:.93;
    font-family:"Roboto Condensed",Arial,sans-serif;font-weight:700;font-size:32px;line-height:1.2;padding:16px 0 0 44px}
  .title-band span{display:block}
  .title-band .line-two{padding-left:10px}
  .front-contact{position:absolute;left:20px;top:630px;font-family:Arimo,Arial,sans-serif;font-size:14px;line-height:1.3}
  .front-blurb{margin-top:10px;font-style:italic;font-size:10.5px;line-height:1.3;width:400px}

  /* Back page */
  .back{position:absolute;left:617px;top:8px;width:570px;height:735px;overflow:hidden;background:var(--panel-grey)}
  .columns{position:absolute;left:0;top:0;width:100%;height:452px;display:flex}
  .column{flex:1;position:relative}
  .column-cap{height:39px}
  .column-body{height:413px;padding:0 7px}
  .yellow .column-cap{background:var(--will-yellow-dark)} .yellow .column-body{background:var(--will-yellow)}
  .coral .column-cap{background:var(--tax-coral-dark)} .coral .column-body{background:var(--tax-coral)}
  .blue .column-cap{background:var(--help-blue-dark)} .blue .column-body{background:var(--help-blue)}
  .green .column-cap{background:var(--offer-green-dark)} .green .column-body{background:var(--offer-green)}
  .topic{position:absolute;left:7px;right:7px;overflow:hidden}
  .topic.first{top:14px;height:122px}
  .topic.second{top:146px;height:150px}
  .topic.third{top:300px;height:150px}
  .topic h3{font-size:6.6px;font-weight:600;line-height:1.3;margin-bottom:6px;text-transform:uppercase}
  .topic p{font-size:5.2px;line-height:1.45;text-align:justify}

  .details{position:absolute;left:0;top:452px;width:100%;height:283px;padding:12px 12px 0 50px}
  .details h3{font-size:7.6px;font-weight:600;margin:0 0 5px;text-transform:uppercase}
  .details p{font-size:6.3px;line-height:1.45;margin-bottom:9px;text-align:justify}
  .back-footer{position:absolute;left:50px;right:12px;bottom:6px;display:flex;justify-content:space-between;font-size:4.6px;opacity:.8}
</style>
</head>
<body>

<section class="front">
  <div class="front-strip"></div>
  <div class="front-photo" role="img" aria-label="Black and white photograph of a man walking along a snowy country road under a stormy sky, with red-tinted trees on the horizon"></div>
  <div class="logo-box">Your Logo Here</div>
  <h1 class="title-band"><span>Is Your Will</span><span class="line-two">UP TO DATE?</span></h1>
  <div class="front-contact">
    <p>http:// www.yourwebsite.com</p>
    <p>derek@hartwellco-mail.co.uk</p>
    <p class="front-blurb">Lorem ipsum dolor sit amet, consectetur adipisicing elit, sed do eiusmod tempor incididunt ut labore et dolore magna aliqua. Ut enim ad minim veniam, quis nostrud exercitation ullamco laboris nisi ut aliquip ex ea commodo consequa</p>
  </div>
</section>

<section class="back">
  <div class="columns">
    <div class="column yellow">
      <div class="column-cap"></div>
      <div class="column-body">
        <div class="topic first"><h3>A Will</h3><p>A Will is one of the most important documents that we should all have. Many people are aware that if they die without having made a Will, then intestate rules apply which means in simple terms, that family assets and cash could end up in the hands of the Treasury.</p></div>
        <div class="topic second"><h3>Amending a Will</h3><p>While many people have looked at and acted upon creating a Will, it is fair to say that for many, the terms and wishes of the Will are often outdated. It is easy to assume that amending a Will frequently is a complicated process which it need not be.</p></div>
        <div class="topic third"><h3>Importance of a Will for your dependants</h3><p>An individual or a family Will is most important in order to ensure that upon death, your estate is dealt with and distributed in accordance with your wishes. This is also to ensure that any family are looked after by those provisions. Not only may family changes and additions affect a family Will, but there are also life changing situations that can have an effect.</p></div>
      </div>
    </div>
    <div class="column coral">
      <div class="column-cap"></div>
      <div class="column-body">
        <div class="topic first"><h3>Current tax position to reduce less tax pay</h3><p>Additionally, consideration needs to be given regularly to the current tax position, with specific regard to Inheritance Tax and how estate values can be legitimately reduced resulting in less tax to pay.</p></div>
        <div class="topic second"><h3>Our financial advisers</h3><p>At Hartwell &amp; Company we have the advantage of our Chartered Accountancy practice background, as well as also being Independent Financial Advisers. We are therefore well placed to advise families on the creation or updating of their Will, and to give advice on how to minimise tax payments.</p></div>
        <div class="topic third"><h3>You need to be updated</h3><p>Even for individuals and families that have had no significant changes in circumstances for many years, very often the beneficiaries may need to be updated, and even the appointment of Executors and Trustees needs to be addressed because very often, these instructions are considerably out of date.</p></div>
      </div>
    </div>
    <div class="column blue">
      <div class="column-cap"></div>
      <div class="column-body">
        <div class="topic first"><h3>Our assistance for Will</h3><p>A Will and all of its complex implications should be reviewed every one or two years and it is an extremely simple process to do this with our assistance.</p></div>
        <div class="topic second"><h3>Reliability for tax</h3><p>So far as minimising payments for tax there are a wide range of effective methods that help do this. As general examples, there can be gifts made to family or a partner, gifts to friends, charitable donations, the use of insurance products to help settle tax liability as well as looking at placing assets into Trust.</p></div>
        <div class="topic third"><h3>Our experience for trusts</h3><p>We have a wealth of experience in setting up the different types of Trust that exist and can help you easily understand how they would work for you.</p></div>
      </div>
    </div>
    <div class="column green">
      <div class="column-cap"></div>
      <div class="column-body">
        <div class="topic first"><h3>Our offers for mitigating possible inheritance tax liabilities</h3><p>So far as mitigating possible Inheritance Tax liabilities on the estate, we also offer the benefit of an asset and investment review at no cost. The individual or family assets are carefully considered, along with your requirements of income and growth.</p></div>
        <div class="topic second"><h3>Initial implications of your decision</h3><p>At the initial meeting or conference call we discuss all of these implications and will prepare a report and recommendations for your consideration, again free of charge. If you decide to act upon any of the recommendations, then any fees can be discussed and agreed at that stage.</p></div>
        <div class="topic third"><h3>No initial costs</h3><p>All in all, whether you require assistance in preparing or updating a Will, or receiving independent advice regarding your estate assets or investments, these functions are carried out by us at no initial costs or charges.</p></div>
      </div>
    </div>
  </div>

  <div class="details">
    <h3>Our method of preparation of Will and charges</h3>
    <p>When looking at preparation of a Will, there are hundreds of questions that could be considered appropriate. However, with our experience and knowledge, and bespoke software this process can be covered within an initial meeting of less than one hour. You will have the re-assurance of knowing that every aspect has been carefully considered in preparing a Will to your circumstances and wishes. The initial meeting and any follow up meetings are completely free of all cost and charges, and can be held at either our offices, or at your home if preferred. Thereafter, we will prepare a draft Will for you, and give you confirmation as to the charges. In most cases, an individual or family Will would not normally involve charges in excess of £100.</p>
    <h3>No hidden charges</h3>
    <p>At every step of the way there are never hidden charges or fees that you will be asked to be paid. We have over 30 years of experience in these market places, and value the service we give our clients and the reputation we gain from it.</p>
    <h3>Consideration of Will</h3>
    <p>We consider the review of a Will should be carried out at a minimum of every two years and it is a very small financial budget to allow for, against having the satisfaction of knowing these important matters are reflecting your current views, circumstances and wishes.</p>
    <h3>Our proud services and clients</h3>
    <p>The same can be said for any trust and investment matters and any estate advice given. We are extremely proud and confident of the service we provide, and if any of our clients decide they do not wish to act upon the advice given, then they at least have had the benefit of a thorough review together with a recommendation without obligations of any sort.</p>
    <h3>Contact us</h3>
    <p>To discuss these matters further or to make arrangements for a meeting please call our offices or email to derek@hartwellco-mail.co.uk</p>
    <div class="back-footer"><span>https://www.yourwebsite.com</span><span>© 2013 All Rights Reserved</span></div>
  </div>
</section>

</body>
</html>
```